GLOW NOW 14 DAY Challange

looking to make a poster that needs to be 36" wide x24"tall design graphic . Check out the added file as it is a rough draft of the material I would like it to say.

Phone number 555-014-2736 www.rbchiropractic..com

Adults aged 25-45 high income adults needing to make changes in dies and lose weight

```html
<!DOCTYPE html>
<html lang="en">
<head>
<meta charset="utf-8">
<title>GLOW NOW 14 DAY Challange</title>
<link href="https://fonts.googleapis.com/css2?family=Acme&family=Baloo+2:wght@800&family=Gelasio&family=Lilita+One&display=swap" rel="stylesheet">
<style>
  :root {
    --backdrop: #e9e6df;
    --card: #fdfcf5;
    --red: #e3202a;
    --navy: #2f2d78;
    --maroon: #7c1416;
    --yellow: #f2ea1a;
    --ink-light: #ffffff;
    --ornament: #35306f;
  }
  * { margin: 0; padding: 0; box-sizing: border-box; }
  html, body { width: 1200px; height: 1181px; overflow: hidden; background: var(--backdrop); }
  .canvas { position: relative; width: 1200px; height: 1181px; }
  .card {
    position: absolute; left: 79px; top: 219px; width: 1042px; height: 735px;
    background: var(--card);
  }
  .title {
    position: absolute; left: 0; width: 100%; top: 34px; text-align: center;
    font-family: "Baloo 2", sans-serif; font-weight: 800; font-size: 50px;
    color: var(--red); line-height: 1;
  }
  .flourish {
    position: absolute; top: 31px; width: 152px; height: 80px;
    background: linear-gradient(90deg, rgba(53,48,111,0.15), rgba(53,48,111,0.55));
    border-radius: 40px;
  }
  .flourish--left { left: 39px; }
  .flourish--right { right: 39px; transform: scaleX(-1); }
  .band { position: absolute; top: 136px; height: 324px; }
  .band--steps { left: 0; width: 525px; background: var(--navy); }
  .band--questions { left: 521px; width: 521px; background: var(--maroon); }
  .scroll-divider {
    position: absolute; left: 496px; top: 129px; width: 50px; height: 340px;
    background: var(--yellow); border: 3px solid var(--navy); border-radius: 25px;
  }
  .steps {
    position: absolute; left: 76px; top: 42px; list-style: none;
    font-family: "Acme", sans-serif; font-size: 25px; line-height: 35px; color: var(--ink-light);
  }
  .steps .gap { margin-top: 34px; }
  .questions {
    position: absolute; left: 57px; top: 44px; list-style: none;
    font-family: "Gelasio", serif; font-size: 33px; line-height: 43.5px; color: var(--ink-light);
  }
  .cta {
    position: absolute; left: 0; width: 100%; top: 494px; text-align: center;
    font-family: "Lilita One", sans-serif; font-size: 40px; color: var(--yellow);
    -webkit-text-stroke: 2px var(--navy); paint-order: stroke fill; line-height: 1;
  }
  .phone-row {
    position: absolute; left: 0; width: 100%; top: 548px;
    display: flex; justify-content: center; align-items: center; gap: 14px;
  }
  .phone-mark { width: 40px; height: 34px; background: var(--red); border-radius: 50%; }
  .phone {
    font-family: "Acme", sans-serif; font-size: 40px; letter-spacing: 5px;
    color: var(--navy); line-height: 1;
  }
  .brand {
    position: absolute; left: 0; width: 100%; top: 610px; text-align: center;
    font-family: "Acme", sans-serif; font-size: 50px; color: var(--navy); line-height: 1;
    letter-spacing: 2px;
  }
  .website {
    position: absolute; left: 0; width: 100%; top: 694px; text-align: center;
    font-family: "Acme", sans-serif; font-size: 24px; color: var(--navy); line-height: 1;
  }
</style>
</head>
<body>
<main class="canvas">
  <article class="card">
    <div class="flourish flourish--left" role="img" aria-label="Decorative navy flourish ornament"></div>
    <h1 class="title">Glow Now 14 Day Challange</h1>
    <div class="flourish flourish--right" role="img" aria-label="Decorative navy flourish ornament"></div>

    <section class="band band--steps">
      <ul class="steps">
        <li>L - Lives Relax Supplements</li>
        <li>O - Omega 3 supplements</li>
        <li>V - Vit D Supplements</li>
        <li>E - Eat Fruts + Veggies</li>
        <li class="gap">K - Keba Homemade Probiotic</li>
        <li>C - Chiroplactic Adjestments</li>
      </ul>
    </section>

    <section class="band band--questions">
      <ul class="questions">
        <li>Do you have Allergies ?</li>
        <li>Need to lose weight ?</li>
        <li>Feel tired ?</li>
        <li>Have Neck or back Pain ?</li>
        <li>Contain .............</li>
      </ul>
    </section>

    <div class="scroll-divider" role="img" aria-label="Yellow scroll ornament dividing the two panels"></div>

    <p class="cta">Call today for Details</p>
    <div class="phone-row">
      <span class="phone-mark" role="img" aria-label="Red flame ornament"></span>
      <span class="phone">555-014-2736</span>
      <span class="phone-mark" role="img" aria-label="Red flame ornament"></span>
    </div>
    <p class="brand">RB Chiropractic</p>
    <p class="website">www.rbchiropractic..com</p>
  </article>
</main>
</body>
</html>
```